Quelvar Website

We need a web design for our company based in Sydney. Our company does many and varied acitivities. From private investments, licencing, business consultacy, payment solutions.

Our services focus on our client’s critical opportunities. We provide a range of services including strategy, marketing, compliance, organization and technology.

We can unlock your growth and potential and deliver on core strategy. We add value and bring extensive expertise in optimizing your results.

We provide also provide the following services:

 private investments,
 licensing,
 business consultancy,
 payment solutions.

Target Market(s)

Businesses

Coding

Coded - Design and coding required

Number of Pages Required

3 page

Colors

Designer to choose colors to be used in the design.

Requirements
Must have
• Corporate look and feel. two touch points, email info@quelvar.com.au and a phone number TBA
• MUST include logos and branding from attached
Nice to have
• photos

```html
<!DOCTYPE html>
<html lang="en">
<head>
<meta charset="utf-8">
<title>Quelvar Private Investments</title>
<link href="https://fonts.googleapis.com/css2?family=Heebo:wght@100;200;300;400;500;700&display=swap" rel="stylesheet">
<style>
:root{
  --black:#0b0b0c;
  --blue:#2f82cf;
  --blue-deep:#1f6fbd;
  --light-bg:#eef1f5;
  --white:#ffffff;
  --text:#333a42;
  --muted:#666d75;
  --line:#c9d3dd;
  --footer-text:#d8d8d8;
}
*{margin:0;padding:0;box-sizing:border-box}
html,body{width:1200px;height:2917px;overflow:hidden}
body{position:relative;font-family:"Heebo",Arial,sans-serif;color:var(--text);background:var(--white)}
.abs{position:absolute}
.center{text-align:center;left:0;width:1200px}

/* header */
.site-header{left:0;top:0;width:1200px;height:95px;background:var(--black)}
.brand{left:101px;top:22px;font-size:42px;font-weight:700;color:var(--blue);display:flex;align-items:center;gap:12px}
.brand .dot{width:16px;height:16px;border-radius:50%;background:var(--blue)}
.nav{left:0;top:36px;width:1200px;font-size:15px;color:var(--white)}
.nav span{position:absolute;transform:translateX(-50%);white-space:nowrap}
.nav .active{color:var(--blue)}

/* hero */
.hero{left:0;top:95px;width:1200px;height:610px;background:linear-gradient(180deg,#4a5560 0%,#39434d 45%,#262d35 100%)}
.hero-title{top:245px;font-size:72px;font-weight:200;color:var(--white);letter-spacing:1px}
.hero-sub{top:328px;font-size:18px;color:var(--white)}
.btn-start{left:515px;top:379px;width:170px;height:41px;background:var(--blue);color:var(--white);font-size:19px;font-weight:700;display:flex;align-items:center;justify-content:center;letter-spacing:.5px}
.hero-arrow{top:380px}

/* services */
.services{left:0;top:612px;width:1200px;height:535px;background:var(--light-bg)}
.section-title{font-size:36px;font-weight:700;color:var(--black)}
.card{top:788px;width:234px;height:258px;background:var(--white);border:1px solid #dde3ea;text-align:center}
.card svg{margin-top:34px}
.card h3{margin-top:10px;font-size:20px;font-weight:500;color:var(--blue)}
.card p{margin:14px 20px 0;font-size:13px;line-height:20px;color:var(--muted)}

/* about */
.about{left:0;top:1147px;width:1200px;height:438px;background:linear-gradient(180deg,#3388d2 0%,#2d7fc9 60%,#5b9fd8 100%)}
.about-title{top:1225px;font-size:38px;font-weight:700;color:var(--white)}
.about-text{left:130px;width:940px;text-align:center;font-size:18px;line-height:27px;color:var(--white);font-weight:300}

/* testimonials */
.testi-title{top:1665px;font-size:36px;font-weight:300;color:var(--black)}
.quote-mark{left:96px;top:1730px;font-size:80px;line-height:1;color:#c8ced4;font-weight:700}
.quote{left:140px;width:920px;top:1752px;text-align:center;font-size:18px;line-height:25px;font-style:italic;color:var(--text);font-weight:300}
.avatar{border-radius:50%;background:radial-gradient(circle at 50% 40%,#9ba3ab,#3c4248)}
.avatar-ring{left:524px;top:1842px;width:152px;height:152px;border-radius:50%;background:#cfe3f5}
.testi-line{left:124px;top:2011px;width:952px;height:2px;background:var(--line)}
.testi-line-active{left:558px;top:2009px;width:84px;height:5px;background:var(--blue)}
.testi-name{top:2032px;font-size:19px;font-weight:700;color:var(--blue)}

/* quick contact */
.contact{left:0;top:2140px;width:1200px;height:400px;background:linear-gradient(180deg,#3a3e44 0%,#26292e 55%,#15171a 100%)}
.contact-title{top:2195px;font-size:38px;font-weight:700;color:var(--white)}
.contact-text{left:330px;width:540px;top:2255px;text-align:center;font-size:18px;line-height:22px;color:var(--white);font-weight:300}
.touch{top:2322px;font-size:36px;font-weight:300;color:var(--white);display:flex;align-items:center;gap:10px;white-space:nowrap}
.btn-touch{left:515px;top:2414px;width:172px;height:44px;border:2px solid var(--white);color:var(--white);font-size:16px;font-weight:500;display:flex;align-items:center;justify-content:center}

/* footer */
.footer{left:0;top:2540px;width:1200px;height:377px;background:var(--black)}
.footer-brand{left:101px;top:2625px;font-size:44px;font-weight:700;color:var(--blue);display:flex;align-items:center;gap:12px}
.footer-brand .dot{width:16px;height:16px;border-radius:50%;background:var(--blue)}
.footer-blurb{left:101px;top:2696px;width:250px;font-size:11px;line-height:16px;color:#4a4e54}
.read-more{left:101px;top:2768px;font-size:12px;color:var(--blue)}
.footer-head{font-size:14px;font-weight:500;color:var(--blue);letter-spacing:.5px}
.footer-rule{height:2px;background:#333}
.footer-rule i{display:block;width:56px;height:2px;background:var(--white)}
.footer-link{font-size:12px;color:var(--white)}
.footer-contact{font-size:12px;color:var(--white);line-height:28px}
.footer-bottom-line{left:101px;top:2849px;width:998px;height:1px;background:#222}
.copyright{top:2872px;font-size:11px;color:#4a4e54}
</style>
</head>
<body>

<header class="abs site-header">
  <div class="abs brand"><span class="dot"></span>Quelvar</div>
  <nav class="abs nav">
    <span class="active" style="left:490px">Home</span>
    <span style="left:591px">About Us</span>
    <span style="left:716px">Our Services</span>
    <span style="left:852px">Testimonials</span>
    <span style="left:961px">Blog</span>
    <span style="left:1062px">Contact Us</span>
  </nav>
</header>

<section class="abs hero" role="img" aria-label="Business team working around a meeting table with laptops"></section>
<h1 class="abs center hero-title">QUELVAR PRIVATE INVESTMENTS</h1>
<p class="abs center hero-sub">We provide a range of services including strategy, marketing, compliance, organisation and technology.</p>
<div class="abs btn-start">START NOW !</div>
<svg class="abs hero-arrow" style="left:34px" width="16" height="36" viewBox="0 0 16 36"><path d="M14 2 2 18l12 16" fill="none" stroke="#fff" stroke-width="2"/></svg>
<svg class="abs hero-arrow" style="left:1136px" width="16" height="36" viewBox="0 0 16 36"><path d="M2 2l12 16L2 34" fill="none" stroke="#fff" stroke-width="2"/></svg>

<section class="abs services"></section>
<svg class="abs" style="left:0;top:600px" width="1200" height="110" viewBox="0 0 1200 110">
  <path d="M0 110 Q600 -60 1200 110 L1200 110 L0 110Z" fill="var(--light-bg)"/>
  <path d="M0 104 Q600 -66 1200 104" fill="none" stroke="var(--blue)" stroke-width="5"/>
</svg>
<h2 class="abs center section-title" style="top:695px">OUR SERVICES</h2>

<svg class="abs" style="left:68px;top:892px" width="22" height="52" viewBox="0 0 22 52"><path d="M20 2 2 26l18 24" fill="none" stroke="#aab2bb" stroke-width="2"/></svg>
<svg class="abs" style="left:1112px;top:892px" width="22" height="52" viewBox="0 0 22 52"><path d="M2 2l18 24L2 50" fill="none" stroke="#aab2bb" stroke-width="2"/></svg>

<article class="abs card" style="left:101px">
  <svg width="70" height="66" viewBox="0 0 70 66" fill="none" stroke="var(--blue)" stroke-width="2.5">
    <rect x="4" y="48" width="8" height="14"/><rect x="18" y="40" width="8" height="22"/><rect x="32" y="30" width="8" height="32"/><rect x="46" y="18" width="8" height="44"/>
    <path d="M6 36 52 6M44 6h8v8"/><circle cx="14" cy="16" r="9"/><path d="M14 10v12"/>
  </svg>
  <h3>Private Investments</h3>
  <p>Sed do eiusmod tempor incididunt ut labore et dolore magna aliqua. Ut enim ad minim...</p>
</article>
<article class="abs card" style="left:356px">
  <svg width="70" height="66" viewBox="0 0 70 66" fill="none" stroke="var(--blue)" stroke-width="2.5">
    <path d="M14 4h30v38H14z"/><path d="M20 14h18M20 22h18M20 30h10"/>
    <circle cx="44" cy="46" r="10"/><path d="M38 54l-4 10 6-3 4 4 2-9"/>
  </svg>
  <h3>Licensing</h3>
  <p>Sed do eiusmod tempor incididunt ut labore et dolore magna aliqua. Ut enim ad minim...</p>
</article>
<article class="abs card" style="left:611px">
  <svg width="90" height="66" viewBox="0 0 90 66" fill="none" stroke="var(--blue)" stroke-width="2.5">
    <circle cx="36" cy="33" r="29"/><circle cx="36" cy="33" r="19"/><circle cx="36" cy="33" r="9"/>
    <path d="M36 33h48M76 27l8 6-8 6"/>
  </svg>
  <h3>Business Consultancy</h3>
  <p>Sed do eiusmod tempor incididunt ut labore et dolore magna aliqua. Ut enim ad minim...</p>
</article>
<article class="abs card" style="left:866px">
  <svg width="90" height="66" viewBox="0 0 90 66" fill="none" stroke="var(--blue)" stroke-width="2.5">
    <rect x="6" y="16" width="70" height="44" rx="4"/><path d="M6 28h70" stroke-width="6"/><path d="M14 44h22M50 48h18"/>
    <circle cx="76" cy="14" r="10" fill="var(--blue)"/><path d="M71 12h10M71 16h10" stroke="#fff" stroke-width="2"/>
  </svg>
  <h3>Payment Solutions</h3>
  <p>Sed do eiusmod tempor incididunt ut labore et dolore magna aliqua. Ut enim ad minim...</p>
</article>

<section class="abs about" role="img" aria-label="Blue tinted desk with business charts and documents"></section>
<h2 class="abs center about-title">ABOUT QUELVAR</h2>
<p class="abs about-text" style="top:1286px">But I must explain to you how all this mistaken idea of denouncing pleasure and praising pain was born and I will give you a complete account of the system, and expound the actual teachings of the great explorer of the truth, the master-builder of human happiness.</p>
<p class="abs about-text" style="top:1388px">Quis autem vel eum iure reprehenderit qui in ea voluptate velit esse quam nihil molestiae consequatur, vel illum qui dolorem eum fugiat quo voluptas nulla pariatur.</p>

<h2 class="abs center testi-title">WHAT OUR CLIENTS SAY?</h2>
<div class="abs quote-mark">“</div>
<p class="abs quote">At vero eos et accusamus et iusto odio dignissimos ducimus qui blanditiis praesentium voluptatum deleniti atque corrupti quos dolores et quas molestias excepturi sint occaecati cupiditate non provident</p>
<svg class="abs" style="left:100px;top:1892px" width="26" height="54" viewBox="0 0 26 54"><path d="M24 2 2 27l22 25" fill="none" stroke="#b8c0c8" stroke-width="2"/></svg>
<svg class="abs" style="left:1076px;top:1892px" width="26" height="54" viewBox="0 0 26 54"><path d="M2 2l22 25L2 52" fill="none" stroke="#b8c0c8" stroke-width="2"/></svg>
<div class="abs avatar" style="left:167px;top:1871px;width:94px;height:94px" role="img" aria-label="Client portrait"></div>
<div class="abs avatar" style="left:305px;top:1871px;width:94px;height:94px" role="img" aria-label="Client portrait"></div>
<div class="abs avatar-ring"></div>
<div class="abs avatar" style="left:534px;top:1852px;width:132px;height:132px;border:4px solid #fff" role="img" aria-label="Portrait of John Doe"></div>
<div class="abs avatar" style="left:785px;top:1871px;width:94px;height:94px" role="img" aria-label="Client portrait"></div>
<div class="abs avatar" style="left:922px;top:1871px;width:94px;height:94px" role="img" aria-label="Client portrait"></div>
<div class="abs testi-line"></div>
<div class="abs testi-line-active"></div>
<div class="abs center testi-name">JOHN DOE</div>

<section class="abs contact" role="img" aria-label="City skyline at dusk"></section>
<h2 class="abs center contact-title">QUICK CONTACT</h2>
<p class="abs contact-text">Dantes remained confused and silent by this explanation of the thoughts which had unconsciously</p>
<div class="abs touch" style="left:225px">
  <svg width="30" height="30" viewBox="0 0 24 24"><path fill="#fff" d="M6.6 10.8a15.1 15.1 0 0 0 6.6 6.6l2.2-2.2c.3-.3.7-.4 1-.2 1.1.4 2.3.6 3.6.6.6 0 1 .4 1 1V20c0 .6-.4 1-1 1A17 17 0 0 1 3 4c0-.6.4-1 1-1h3.5c.6 0 1 .4 1 1 0 1.3.2 2.5.6 3.6.1.3 0 .7-.2 1z"/></svg>
  1-800-555-0147
</div>
<div class="abs touch" style="left:628px">
  <svg width="36" height="28" viewBox="0 0 36 28"><rect width="36" height="28" rx="2" fill="#fff"/><path d="M2 3l16 13L34 3" fill="none" stroke="#2a2e33" stroke-width="3"/></svg>
  info@quelvar.com.au
</div>
<div class="abs btn-touch">GET IN TOUCH</div>

<footer class="abs footer"></footer>
<div class="abs footer-brand"><span class="dot"></span>Quelvar</div>
<p class="abs footer-blurb">But I must explain to you how all this mistaken idea of denouncing pleasure and praising pain was born and I will give you a complete...</p>
<div class="abs read-more">read more...</div>

<div class="abs footer-head" style="left:447px;top:2603px">QUICK LINKS</div>
<div class="abs footer-rule" style="left:447px;top:2634px;width:136px"><i></i></div>
<div class="abs footer-link" style="left:447px;top:2668px">Home</div>
<div class="abs footer-link" style="left:447px;top:2696px">About Us</div>
<div class="abs footer-link" style="left:447px;top:2724px">Our Services</div>
<div class="abs footer-link" style="left:447px;top:2753px">Testimonials</div>
<div class="abs footer-link" style="left:636px;top:2668px">Terms &amp; Conditions</div>
<div class="abs footer-link" style="left:636px;top:2696px">Privacy Policy</div>
<div class="abs footer-link" style="left:636px;top:2724px">Contact</div>

<div class="abs footer-head" style="left:862px;top:2603px">CONTACT US</div>
<div class="abs footer-rule" style="left:862px;top:2634px;width:190px"><i></i></div>
<svg class="abs" style="left:862px;top:2669px" width="10" height="14" viewBox="0 0 10 14"><path fill="var(--blue)" d="M5 0a5 5 0 0 0-5 5c0 4 5 9 5 9s5-5 5-9a5 5 0 0 0-5-5zm0 7a2 2 0 1 1 0-4 2 2 0 0 1 0 4z"/></svg>
<div class="abs footer-contact" style="left:883px;top:2662px">QUELVAR, Street Address, City Name,<br>Country Name, Pin Code.</div>
<svg class="abs" style="left:862px;top:2725px" width="12" height="12" viewBox="0 0 24 24"><path fill="var(--blue)" d="M6.6 10.8a15.1 15.1 0 0 0 6.6 6.6l2.2-2.2c.3-.3.7-.4 1-.2 1.1.4 2.3.6 3.6.6.6 0 1 .4 1 1V20c0 .6-.4 1-1 1A17 17 0 0 1 3 4c0-.6.4-1 1-1h3.5c.6 0 1 .4 1 1 0 1.3.2 2.5.6 3.6.1.3 0 .7-.2 1z"/></svg>
<div class="abs footer-contact" style="left:883px;top:2717px">1-800-555-0147</div>
<svg class="abs" style="left:862px;top:2754px" width="13" height="10" viewBox="0 0 13 10"><rect width="13" height="10" rx="1" fill="var(--blue)"/><path d="M1 1l5.5 4.5L12 1" fill="none" stroke="#000" stroke-width="1.3"/></svg>
<div class="abs footer-contact" style="left:883px;top:2745px">info@quelvar.com.au</div>

<div class="abs footer-bottom-line"></div>
<div class="abs center copyright">© 2018 QUELVAR . All right reserved . Term of Use</div>

</body>
</html>
```